Website design for SaaS -solution

We are B2B SaaS company. (Korlet.io) Our software brings leads by enriching company profiles with external data. We want to take load off from marketing and sales directors by bringing them sales leads.

Our core values that we want to communicate:
-Data driven
-Easy going and easy to use
-Sincere and honest
-Humble
-lively

We would like to see designs that obey our colours (logos attached) but also the website should be lively and visual / photo intensive. We only use few sentences to power our message. Here are few examples:

http://www.plovista.com/
https://www.zundel.com/

We will also make a video that we post in the front cover. Our current website is www.korlet.io. The font we would like to use is Avenir Next or similar

• Avenir Next

0455a3
ec1f27
9bcb3c
85acd3

• 1 page: the main page (attached is brief) (This is most important one)
• 2. page: , a design where we can post content such as slides, e-papers etc (e.g.. http://www.brightmoor.com/eu/industries/)
• 3. page: a basic template that can be used for various needs ( team-page, jobs, page, etc)

```html
<!DOCTYPE html>
<html lang="en">
<head>
<meta charset="utf-8">
<title>Korlet – Sales leads from company data</title>
<link rel="stylesheet" href="https://fonts.googleapis.com/css2?family=Nunito+Sans:wght@400;600;700;800&display=swap">
<style>
:root{
  --brand-blue:#0455a3;
  --brand-navy:#173a6b;
  --brand-sky:#85acd3;
  --brand-red:#ec1f27;
  --brand-green:#9bcb3c;
  --ink:#3a3f47;
  --muted:#7a8089;
  --topbar:#2a2d31;
  --band:#dfeaf6;
  --testimonial:#1e2630;
  --footer:#eef0f2;
  --bottom:#23262a;
  --white:#ffffff;
}
*{box-sizing:border-box;margin:0;padding:0}
html,body{width:755px;height:1200px;overflow:hidden}
body{font-family:"Nunito Sans",Arial,sans-serif;color:var(--ink);background:var(--white);font-size:8px;line-height:1.45;position:relative}
a{color:inherit;text-decoration:none}

/* top utility bar */
.topbar{height:20px;background:var(--topbar);display:flex;align-items:center;justify-content:space-between;padding:0 70px}
.social-squares{display:flex;gap:3px}
.social-squares span{width:12px;height:12px;border-radius:2px;display:block}
.utility-links{display:flex;gap:8px;color:#c9ccd1;font-size:6.5px;letter-spacing:.4px;text-transform:uppercase}

/* header */
.site-header{height:85px;display:flex;align-items:center;justify-content:space-between;padding:0 70px;border-bottom:1px solid #e4e6ea}
.brand{display:flex;align-items:center;gap:8px;font-size:26px;font-weight:700;color:var(--brand-navy);letter-spacing:.5px}
.brand-dot{width:16px;height:16px;border-radius:50%;background:var(--brand-blue)}
.main-nav{display:flex;gap:26px;font-size:9px;color:var(--ink)}

/* hero */
.hero{position:relative;height:273px;overflow:hidden}
.hero-photo{position:absolute;inset:0;background:linear-gradient(180deg,#1b2b47 0%,#2c4266 35%,#4a5f7e 60%,#2a2f3c 100%)}
.hero-glow{position:absolute;inset:0;background:radial-gradient(ellipse at 30% 75%,rgba(255,196,120,.35),transparent 55%),radial-gradient(ellipse at 70% 85%,rgba(255,220,160,.25),transparent 50%)}
.hero-intro{position:absolute;left:95px;top:88px;width:155px;background:rgba(220,232,247,.85);padding:8px 9px;color:var(--brand-navy);font-size:7.5px;font-weight:600}
.signup{position:absolute;left:95px;top:210px;display:flex}
.signup-input{width:145px;height:17px;background:var(--white);font-size:6.5px;color:#9aa0a8;padding:4px 6px}
.signup-button{height:17px;padding:0 10px;background:var(--brand-blue);color:var(--white);font-size:6.5px;font-weight:700;display:flex;align-items:center;letter-spacing:.5px}
.hero-card{position:absolute;left:467px;width:272px;background:rgba(230,238,248,.88);padding:8px 12px 10px;text-align:center}
.hero-card.about{top:12px;height:115px}
.hero-card.event{top:138px;height:124px}
.hero-card h2{font-size:15px;font-weight:700;color:var(--brand-navy);text-align:left;margin-bottom:6px}
.hero-card .card-copy{background:var(--brand-blue);color:var(--white);font-size:7px;text-align:left;padding:5px 7px;margin-bottom:7px}
.event-title{font-size:14px;font-weight:700;color:var(--brand-navy);text-align:left}
.event-name{font-size:28px;font-weight:800;color:var(--brand-navy);text-align:right;line-height:1.05;letter-spacing:1px}
.event-date{font-size:7px;color:var(--brand-blue);text-align:right;margin-bottom:6px}
.btn{display:inline-block;background:var(--brand-blue);color:var(--white);font-size:7px;font-weight:700;padding:4px 14px}
.slider-arrow{position:absolute;top:126px;width:16px;height:16px;border-radius:50%;background:rgba(255,255,255,.25)}
.slider-arrow.prev{left:4px}
.slider-arrow.next{right:4px}

/* welcome */
.welcome{height:175px;display:flex;gap:24px;padding:22px 70px 0}
.video-frame{width:207px;height:118px;background:linear-gradient(135deg,#3e4652,#9aa3ae);position:relative;flex:none}
.play-button{position:absolute;left:50%;top:50%;transform:translate(-50%,-50%)}
.welcome-copy h1{font-size:15px;color:var(--brand-blue);font-weight:700;margin-bottom:2px}
.welcome-copy .lead{font-size:8px;color:var(--ink);font-weight:600;margin-bottom:5px}
.welcome-copy p{font-size:6.8px;color:var(--muted);margin-bottom:4px}
.welcome-copy .more{color:var(--brand-blue);font-weight:700}

/* features band */
.features{height:255px;background:linear-gradient(180deg,#eaf1f9,var(--band));text-align:center;padding-top:38px}
.features h2{font-size:14px;color:var(--brand-blue);font-weight:700}
.features .subtitle{font-size:7px;color:var(--muted);margin-bottom:22px}
.feature-list{display:flex;justify-content:center;gap:95px}
.feature{width:110px}
.feature-icon{width:50px;height:50px;border-radius:50%;background:var(--brand-blue);margin:0 auto 6px;display:flex;align-items:center;justify-content:center}
.feature h3{font-size:8.5px;color:var(--brand-navy);font-weight:700}
.feature p{font-size:6.5px;color:var(--muted)}

/* testimonials */
.testimonials{height:180px;background:radial-gradient(ellipse at 50% 40%,#2f3b4b,var(--testimonial) 70%);text-align:center;color:var(--white);padding-top:14px}
.testimonials h2{font-size:11px;font-weight:700;letter-spacing:1px}
.rule{width:40px;height:1px;background:rgba(255,255,255,.5);margin:5px auto 9px}
.client-photo{width:48px;height:48px;border-radius:50%;background:linear-gradient(160deg,#c9ccd2,#7d8694);border:2px solid var(--white);margin:0 auto 11px}
.quote{width:470px;margin:0 auto 9px;font-size:7px;color:#d6dae0;font-style:normal}
.attribution{display:flex;justify-content:center;align-items:center;gap:14px;font-size:7.5px;font-weight:700}
.round-arrow{width:13px;height:13px;border:1px solid rgba(255,255,255,.6);border-radius:50%;display:flex;align-items:center;justify-content:center}

/* footer */
.site-footer{height:195px;background:var(--footer);display:flex;gap:32px;padding:16px 70px 0}
.footer-col{flex:1}
.footer-col h4{font-size:8.5px;color:var(--ink);font-weight:700;margin-bottom:7px}
.contact-line{display:flex;align-items:center;gap:6px;font-size:6.5px;color:var(--muted);margin-bottom:6px}
.update{font-size:6.3px;color:var(--muted);margin-bottom:6px}
.update .when{color:var(--brand-blue);display:block}
.about-links li{list-style:none;font-size:6.5px;color:var(--muted);margin-bottom:4px}
.follow-copy{font-size:6.5px;color:var(--muted);margin-bottom:8px}
.follow-circles{display:flex;gap:5px}
.follow-circles span{width:15px;height:15px;border-radius:50%;background:#5b6068;display:block}
.bottom-bar{position:absolute;left:0;right:0;bottom:0;height:17px;background:var(--bottom);color:#9ba0a7;font-size:6px;display:flex;align-items:center;justify-content:space-between;padding:0 70px}
</style>
</head>
<body>

<div class="topbar">
  <div class="social-squares">
    <span style="background:#3b8fd6"></span>
    <span style="background:#f0a020"></span>
    <span style="background:#2f5a9e"></span>
    <span style="background:#d23a2f"></span>
    <span style="background:#c2272d"></span>
  </div>
  <nav class="utility-links"><a href="#">Login</a>|<a href="#">Blog</a>|<a href="#">Contact</a>|<span>+1 (555) 0142 3860</span>|<a href="#">Careers</a></nav>
</div>

<header class="site-header">
  <a class="brand" href="#"><span class="brand-dot"></span>Korlet</a>
  <nav class="main-nav"><a href="#">Home</a><a href="#">Team</a><a href="#">Products</a><a href="#">Customer</a><a href="#">Careers</a></nav>
</header>

<section class="hero">
  <div class="hero-photo" role="img" aria-label="City skyline at night with lit office towers"></div>
  <div class="hero-glow"></div>
  <span class="slider-arrow prev"></span><span class="slider-arrow next"></span>
  <div class="hero-intro">Lorem ipsum dolor sit amet, consectetur adipiscing elit, sed do eiusmod tempor incididunt ut labore magna aliqua ut enim.</div>
  <form class="signup"><div class="signup-input">Enter your email</div><div class="signup-button">SUBMIT</div></form>

  <div class="hero-card about">
    <h2>To know about Korlet</h2>
    <div class="card-copy">Lorem ipsum dolor sit amet, consectetur adipiscing elit, sed do eiusmod tempor incididunt ut labore et dolore magna aliqua ut enim ad minim veniam quis nostrud.</div>
    <a class="btn" href="#">Learn More</a>
  </div>
  <div class="hero-card event">
    <div class="event-title">The Growth Circle</div>
    <div class="event-name">SUMMIT</div>
    <div class="event-date">19 April 2016 San Francisco</div>
    <a class="btn" href="#">Learn More</a>
  </div>
</section>

<section class="welcome">
  <div class="video-frame" role="img" aria-label="Video still of a presenter at a whiteboard">
    <svg class="play-button" width="30" height="30" viewBox="0 0 30 30"><circle cx="15" cy="15" r="14" fill="rgba(0,0,0,.45)" stroke="#fff" stroke-width="1.2"/><path d="M12 9.5 21 15 12 20.5z" fill="#fff"/></svg>
  </div>
  <div class="welcome-copy">
    <h1>Welcome to Our Korlet</h1>
    <div class="lead">Lorem ipsum dolor sit amet, consectetur</div>
    <p>Lorem ipsum dolor sit amet, consectetur adipiscing elit, sed do eiusmod tempor incididunt ut labore et dolore magna aliqua. Ut enim ad minim veniam, quis nostrud exercitation ullamco laboris nisi ut aliquip ex ea commodo consequat duis aute irure dolor in reprehenderit in voluptate velit esse cillum.</p>
    <p>Lorem ipsum dolor sit amet, consectetur adipiscing elit, sed do eiusmod tempor incididunt ut labore et dolore magna aliqua enim minim veniam nostrud exercitation ullamco. <a class="more" href="#">Continue Reading...</a></p>
  </div>
</section>

<section class="features">
  <h2>Is b2b sale complete the gone digitel ?</h2>
  <p class="subtitle">Lorem ipsum dolor sit amet, consectetur adipiscing elit, sed do eiusmod tempor incididunt ut labore</p>
  <div class="feature-list">
    <div class="feature">
      <div class="feature-icon"><svg width="24" height="22" viewBox="0 0 24 22"><rect x="2" y="12" width="4" height="8" fill="#fff"/><rect x="10" y="7" width="4" height="13" fill="#fff"/><rect x="18" y="2" width="4" height="18" fill="#fff"/></svg></div>
      <h3>Marketing</h3><p>Ut enim ad minim veniam, quis nostrud exercitation</p>
    </div>
    <div class="feature">
      <div class="feature-icon"><svg width="24" height="22" viewBox="0 0 24 22"><path d="M1 2h4l3 12h12l3-9H7" fill="none" stroke="#fff" stroke-width="2"/><circle cx="9" cy="18" r="2" fill="#fff"/><circle cx="19" cy="18" r="2" fill="#fff"/></svg></div>
      <h3>Sales</h3><p>Ut enim ad minim veniam, quis nostrud exercitation</p>
    </div>
    <div class="feature">
      <div class="feature-icon"><svg width="22" height="22" viewBox="0 0 22 22"><circle cx="11" cy="7" r="5" fill="#fff"/><path d="M2 21c0-5 4-8 9-8s9 3 9 8z" fill="#fff"/></svg></div>
      <h3>Industry expert</h3><p>Ut enim ad minim veniam, quis nostrud exercitation</p>
    </div>
  </div>
</section>

<section class="testimonials">
  <h2>TESTIMONIALS</h2>
  <div class="rule"></div>
  <div class="client-photo" role="img" aria-label="Portrait of a client"></div>
  <blockquote class="quote">Magni dolores eos qui ratione voluptatem sequi nesciunt. Neque porro quisquam est, qui dolorem ipsum quia dolor sit amet, consectetur, adipisci velit, sed quia non numquam eius modi tempora incidunt ut labore.</blockquote>
  <div class="attribution">
    <span class="round-arrow"><svg width="6" height="6" viewBox="0 0 6 6"><path d="M4 0.5 1.5 3 4 5.5" fill="none" stroke="#fff"/></svg></span>
    <span>Aron Vale, Job</span>
    <span class="round-arrow"><svg width="6" height="6" viewBox="0 0 6 6"><path d="M2 0.5 4.5 3 2 5.5" fill="none" stroke="#fff"/></svg></span>
  </div>
</section>

<footer class="site-footer">
  <div class="footer-col">
    <h4>Contact us</h4>
    <div class="contact-line"><svg width="8" height="8" viewBox="0 0 8 8"><path d="M1.5 0.5h1.5l.8 2-1 .7a4 4 0 0 0 2 2l.7-1 2 .8v1.5c0 .5-.5 1-1 1A7 7 0 0 1 .5 1.5c0-.5.5-1 1-1z" fill="#7a8089"/></svg>(555) 014-2386</div>
    <div class="contact-line"><svg width="8" height="8" viewBox="0 0 8 8"><path d="M1.5 0.5h1.5l.8 2-1 .7a4 4 0 0 0 2 2l.7-1 2 .8v1.5c0 .5-.5 1-1 1A7 7 0 0 1 .5 1.5c0-.5.5-1 1-1z" fill="#7a8089"/></svg>(555) 014-2387</div>
    <div class="contact-line"><svg width="8" height="8" viewBox="0 0 8 8"><rect x=".5" y="1.5" width="7" height="5" fill="none" stroke="#7a8089"/><path d="M.5 1.5 4 4.5 7.5 1.5" fill="none" stroke="#7a8089"/></svg>info@korlet.io</div>
    <div class="contact-line"><svg width="8" height="8" viewBox="0 0 8 8"><circle cx="4" cy="4" r="3.5" fill="none" stroke="#7a8089"/><path d="M.5 4h7M4 .5v7" stroke="#7a8089" stroke-width=".6"/></svg>www.korlet.io</div>
    <div class="contact-line"><svg width="8" height="9" viewBox="0 0 8 9"><path d="M4 8.5S.8 5.2.8 3.3a3.2 3.2 0 0 1 6.4 0C7.2 5.2 4 8.5 4 8.5z" fill="#7a8089"/></svg>PO Box 4412, Harlow Street 2207</div>
  </div>
  <div class="footer-col">
    <h4>Latest Updates</h4>
    <p class="update">Lorem ipsum dolor sit amet, consectetur adipiscing elit sed do eiusmod <span class="when">2 hours ago</span></p>
    <p class="update">Lorem ipsum dolor sit amet, consectetur adipiscing elit sed do eiusmod <span class="when">5 hours ago</span></p>
    <p class="update">Lorem ipsum dolor sit amet, consectetur adipiscing elit sed do eiusmod <span class="when">1 day ago</span></p>
  </div>
  <div class="footer-col">
    <h4>About us</h4>
    <ul class="about-links">
      <li>Investors</li><li>Careers</li><li>Terms &amp; Conditions of service</li><li>Privacy Policy</li><li>Service Level Agreement</li><li>Brand Commercial Agreement</li>
    </ul>
  </div>
  <div class="footer-col">
    <h4>Follow us</h4>
    <p class="follow-copy">Lorem ipsum dolor sit amet, consectetur adipiscing elit, sed do eiusmod tempor incididunt ut labore.</p>
    <div class="follow-circles"><span></span><span></span><span></span><span></span></div>
  </div>
</footer>

<div class="bottom-bar"><span>Copyright © 2015 Korlet, All right reserved</span><span>1 / 10</span></div>

</body>
</html>
```